Mr Tovel Car Wash Menu Brochure

Front/Back brochure with Car Wash Menu Options & pricing
(size : 8.5" x 3.66" - front/back)

Side 1:
Logo on top
"Wash Menu"
- Grand Tovel - $19
- includes Orla & Finch
- Super Shine Hot Wax
- Kestrel Coat - total surface sealant
- Wheel Bright
- Orla & Finch - $15
- Includes Prime Tovel
- Clear Coat Protectant
- Tire Gloss
- Prime Tovel - $11
- Includes Express Wash
- Triple Foam
- Wheel Cleaner
- Express Wash - $4

*Add-Ons
- Dravenol Ceramic - $5
- Kestrel Coat - $3
- Tire Gloss - $3

*FREE Vacuums with every purchase
* We care about the earth! We recycle our water

SIDE 2:
Mr Tovel Logo on Top
Unlimited Monthly VIP Club
- Grand Tovel - $55
- includes 10% off detail packages
- Orla & Finch - $45
-Prime Tovel - $30
-Express Wash - $20

* one wash tag per vehicle

Target Market(s)

sophisticated customers

Industry/Entity Type

car wash

Colors
0054AA
0677BA
7BADD7
CADEEF
E8F1F8
EE7325
F08F49
F5BC92
FAE3D3
FDF4ED

Requirements
Must have
• pictures/icons to relay what each package entails

```html
<!DOCTYPE html>
<html lang="en">
<head>
<meta charset="utf-8">
<title>Mr Tovel – Wash Menu Rack Cards</title>
<link href="https://fonts.googleapis.com/css2?family=Orbitron:wght@500;600&family=Raleway:ital,wght@1,500&display=swap" rel="stylesheet">
<style>
  :root{
    --backdrop:#d8d8d8;
    --paper:#efeff1;
    --red:#c92029;
    --red-deep:#9b1920;
    --navy:#1f3a5f;
    --blue:#0b5fb0;
    --blue-bright:#1b8fdc;
    --ink-light:#f2f4f8;
    --head-font:"Orbitron", sans-serif;
    --note-font:"Raleway", sans-serif;
  }
  *{box-sizing:border-box;margin:0;padding:0}
  html,body{width:1200px;height:1023px;overflow:hidden;background:var(--backdrop)}
  .card{position:absolute;top:126px;height:766px;background:var(--paper);overflow:hidden;font-family:var(--head-font);color:var(--ink-light)}
  .card--vip{left:233px;width:331px}
  .card--menu{left:630px;width:328px}

  .brand{position:absolute;left:0;right:0;top:40px;text-align:center}
  .brand__name{display:inline-flex;align-items:center;gap:10px;font-size:30px;font-weight:600;color:var(--navy);letter-spacing:1px}
  .brand__dot{width:14px;height:14px;border-radius:50%;background:var(--red)}
  .brand__tag{margin-top:18px;font-size:10.5px;font-weight:600;letter-spacing:3px;color:var(--red)}

  .panel{position:absolute;left:0;right:0;bottom:0}
  .card--vip .panel{top:172px;background:var(--navy)}
  .card--vip .topbar{position:absolute;left:18px;right:18px;top:163px;height:14px;border-radius:8px 8px 0 0;background:var(--blue)}
  .card--menu .panel{top:169px;background:radial-gradient(ellipse at 50% 55%,#e02a30 0%,var(--red) 45%,var(--red-deep) 100%)}
  .card--menu .topbar{position:absolute;left:18px;right:18px;top:160px;height:14px;border-radius:8px 8px 0 0;background:var(--red)}

  .splash{position:absolute;left:0;right:0;top:0}
  .splash--red{height:180px;background:linear-gradient(160deg,var(--red) 30%,var(--red-deep));border-radius:0 0 70% 30% / 0 0 40% 25%}
  .splash--blue{height:150px;background:linear-gradient(170deg,var(--blue-bright) 10%,var(--blue) 70%);border-radius:0 0 60% 35% / 0 0 45% 30%}

  .title{position:absolute;font-weight:600;color:var(--ink-light)}
  .card--vip .title{left:29px;top:20px;font-size:23px;line-height:31px}
  .card--menu .title{left:25px;top:12px;font-size:24px}

  .item{position:absolute;left:26px;right:8px;display:flex;align-items:center;font-weight:600}
  .item__leader{flex:1;border-top:1.5px dashed var(--ink-light);margin:0 8px;opacity:.85}
  .price{width:44px;height:44px;border-radius:50%;display:flex;align-items:center;justify-content:center;font-size:14px;font-weight:600}
  .card--vip .item{font-size:15px}
  .card--vip .price{background:radial-gradient(circle at 65% 30%,#f26a70,var(--red) 45%,var(--red-deep))}
  .card--menu .item{font-size:14px;left:29px}
  .card--menu .price{width:40px;height:40px;background:radial-gradient(circle at 65% 30%,#7fb4e4,var(--blue) 50%,#14396b)}

  .perk{position:absolute;left:26px;font-size:10px;line-height:16px;letter-spacing:1px}
  .bullets{position:absolute;left:32px;list-style:none;font-size:9.5px;line-height:15.3px;letter-spacing:.8px}
  .bullets li::before{content:"•";margin-right:6px}
  .bullets .cont{padding-left:12px}
  .bullets .cont::before{content:""}

  .addons{position:absolute;left:0;right:0;top:488px;height:57px;background:var(--navy);display:flex;align-items:center;padding-left:28px;gap:14px}
  .addons__label{font-size:19px;line-height:21px;font-weight:600}
  .addons__list{list-style:none;font-size:10px;line-height:16px;letter-spacing:.8px}
  .addons__list li::before{content:"•";margin-right:5px}
  .addons__list b{font-size:13px}

  .note{position:absolute;left:0;right:0;text-align:center;font-family:var(--note-font);font-style:italic;font-size:9.5px;line-height:12px}
  .web{position:absolute;left:0;right:0;text-align:center;font-family:var(--note-font);font-style:normal;font-size:12px;letter-spacing:3px}
</style>
</head>
<body>

<section class="card card--vip">
  <header class="brand">
    <div class="brand__name"><span class="brand__dot"></span>MR TOVEL</div>
    <div class="brand__tag">EXPRESS WASH &amp; DETAIL</div>
  </header>
  <div class="topbar"></div>
  <div class="panel">
    <div class="splash splash--red" role="img" aria-label="Red liquid splash with droplets"></div>
    <h2 class="title">UNLIMITED<br>MONTHLY VIP<br>CLUB</h2>

    <div class="item" style="top:236px">GRAND TOVEL<span class="item__leader"></span><span class="price">$55</span></div>
    <p class="perk" style="top:280px">INCLUDES<br>10% OFF DETAIL PACKAGES</p>
    <div class="item" style="top:324px">ORLA &amp; FINCH<span class="item__leader"></span><span class="price">$45</span></div>
    <p class="perk" style="top:366px">INCLUDES<br>10% OFF DETAIL PACKAGES</p>
    <div class="item" style="top:414px">PRIME TOVEL<span class="item__leader"></span><span class="price">$30</span></div>
    <div class="item" style="top:480px">EXPRESS WASH<span class="item__leader"></span><span class="price">$20</span></div>

    <p class="note" style="top:543px">* One Wash Tag Per Vehicle</p>
    <p class="web" style="top:559px">WWW.MRTOVELWASH.COM</p>
  </div>
</section>

<section class="card card--menu">
  <header class="brand">
    <div class="brand__name"><span class="brand__dot"></span>MR TOVEL</div>
    <div class="brand__tag">EXPRESS WASH &amp; DETAIL</div>
  </header>
  <div class="topbar"></div>
  <div class="panel">
    <div class="splash splash--blue" role="img" aria-label="Blue water splash with droplets"></div>
    <h2 class="title">WASH MENU</h2>

    <div class="item" style="top:162px">GRAND TOVEL<span class="item__leader"></span><span class="price">$19</span></div>
    <ul class="bullets" style="top:197px">
      <li>INCLUDES ORLA &amp; FINCH</li>
      <li>SUPER SHINE HOT WAX</li>
      <li>KESTREL COAT -</li>
      <li class="cont">TOTAL SURFACE SEALANT</li>
      <li>WHEEL BRIGHT</li>
    </ul>
    <div class="item" style="top:275px">ORLA &amp; FINCH<span class="item__leader"></span><span class="price">$15</span></div>
    <ul class="bullets" style="top:309px">
      <li>INCLUDES PRIME TOVEL</li>
      <li>CLEAR COAT PROTECTANT</li>
      <li>TIRE GLOSS</li>
    </ul>
    <div class="item" style="top:355px">PRIME TOVEL<span class="item__leader"></span><span class="price">$11</span></div>
    <ul class="bullets" style="top:388px">
      <li>INCLUDES EXPRESS WASH</li>
      <li>TRIPLE FOAM</li>
      <li>WHEEL CLEANER</li>
    </ul>
    <div class="item" style="top:439px">EXPRESS WASH<span class="item__leader"></span><span class="price">$4</span></div>

    <div class="addons">
      <div class="addons__label">ADD<br>ONS</div>
      <ul class="addons__list">
        <li>KESTREL COAT - <b>$3</b></li>
        <li>DRAVENOL CERAMIC - <b>$5</b></li>
        <li>TIRE GLOSS - <b>$3</b></li>
      </ul>
    </div>

    <p class="note" style="top:560px">*FREE Vacuums with every purchase</p>
    <p class="note" style="top:573px">* We care about the earth! We recycle our water</p>
  </div>
</section>

</body>
</html>
```